Verdane apparel business card

We are a clothing manufacturers agent based in London. Our clients are fashion retailers in the UK and Europe. We are looking for a business card design that communicates corporate stability and a creative edge

Target Market(s)

our customers are large international fashion retailers, smaller fashion stores and distributors and designers

Industry/Entity Type

Clothing

```html
<!DOCTYPE html>
<html lang="en">
<head>
<meta charset="utf-8">
<title>Verdane Apparel Business Card</title>
<link rel="stylesheet" href="https://fonts.googleapis.com/css2?family=Cinzel:wght@700&family=Arimo:wght@400&display=swap">
<style>
  :root {
    --backdrop: #e4e4e6;
    --card: #ffffff;
    --ink: #111111;
    --violet-light: #b5519c;
    --violet-deep: #7b2a7e;
    --icon: #8a3a8c;
    --on-band: #ffffff;
  }
  * { box-sizing: border-box; margin: 0; padding: 0; }
  html, body {
    width: 1200px; height: 902px; overflow: hidden;
    background: var(--backdrop);
  }
  .card {
    position: absolute; left: 100px; top: 165px;
    width: 1000px; height: 571px;
    background: var(--card);
    box-shadow: 0 10px 30px rgba(0,0,0,0.18);
    font-family: "Arimo", Arial, sans-serif;
    color: var(--ink);
  }
  .company {
    position: absolute; top: 110px; left: 0; width: 100%;
    text-align: center;
    font-family: "Cinzel", Georgia, serif;
    font-weight: 700; font-size: 37px; letter-spacing: 1px;
  }
  .brand-mark {
    position: absolute; top: 192px; left: 0; width: 100%;
    display: flex; justify-content: center; align-items: center; gap: 14px;
  }
  .brand-mark .dot {
    width: 96px; height: 96px; border-radius: 50%;
    background: var(--ink);
  }
  .brand-mark .name {
    font-family: "Cinzel", Georgia, serif; font-weight: 700;
    font-size: 30px; color: var(--violet-deep);
  }
  .contacts {
    position: absolute; top: 340px; font-size: 25px; line-height: 31px;
  }
  .contacts li { list-style: none; display: flex; align-items: center; gap: 16px; }
  .contacts svg { width: 20px; height: 20px; fill: var(--icon); flex: none; }
  .contacts-online { left: 112px; }
  .contacts-phone { left: 686px; }
  .band { position: absolute; left: 0; bottom: 0; width: 1000px; height: 116px; }
  .band svg { position: absolute; inset: 0; }
  .band .person {
    position: absolute; left: 103px; top: 0; line-height: 116px;
    font-size: 34px; color: var(--on-band);
  }
  .band .role {
    position: absolute; left: 702px; top: 0; line-height: 116px;
    font-size: 22px; color: var(--on-band);
  }
</style>
</head>
<body>
  <main class="card">
    <h1 class="company">VERDANE APPAREL LTD</h1>
    <div class="brand-mark">
      <span class="dot"></span>
      <span class="name">Verdane</span>
    </div>

    <ul class="contacts contacts-online">
      <li>
        <svg viewBox="0 0 20 20" aria-hidden="true"><path d="M2 5h16v10H2z M2 5l8 6 8-6" fill="var(--icon)"/><path d="M3 6l7 5 7-5" stroke="#fff" stroke-width="1.4" fill="none"/></svg>
        hello@verdanemail.com
      </li>
      <li>
        <svg viewBox="0 0 20 20" aria-hidden="true"><circle cx="10" cy="10" r="8.5"/><path d="M1.5 10h17M10 1.5c-4 4.5-4 12.5 0 17M10 1.5c4 4.5 4 12.5 0 17" stroke="#fff" stroke-width="1.2" fill="none"/></svg>
        www.verdaneapparel.com
      </li>
    </ul>

    <ul class="contacts contacts-phone">
      <li>
        020-5550100
        <svg viewBox="0 0 20 20" aria-hidden="true"><path d="M2 7c0-3 16-3 16 0v2h-4V7.5H6V9H2z"/><path d="M5 10h10l2 6H3z"/></svg>
      </li>
      <li>
        075-5550182
        <svg viewBox="0 0 20 20" aria-hidden="true"><rect x="5" y="1" width="10" height="18" rx="2"/><rect x="7" y="4" width="6" height="10" fill="#fff"/></svg>
      </li>
    </ul>

    <div class="band">
      <svg viewBox="0 0 1000 116" aria-hidden="true">
        <polygon points="0,0 441,0 428,116 0,116" fill="var(--violet-light)"/>
        <polygon points="455,0 1000,0 1000,116 441,116" fill="var(--violet-deep)"/>
      </svg>
      <span class="person">Your Name</span>
      <span class="role">Title</span>
    </div>
  </main>
</body>
</html>
```